Packaging Design for Vito Prime

We require an outstanding packaging design for our Vito Prime brand, which offers hydration electrolyte supplements specifically tailored for athletes and sporty individuals.

Benchmark packaging design from aquelle competitor attached. The product packaging contains 20 x 20g sticks of the product.

Target Market

Psychographic: Health-conscious, active lifestyle, values quality, functionality and sustainability.

product description 1:
HYDRATION BOOSTER
Refresh, Replenish, Recharge!

product description 2:
PREMIUM ISOTONIC ELECTROLYTE DRINK
Nutritional Expertise Since 1992.

Existing Logo: to add "since 1992"

Appeal to Target Market: Create a design that resonates with both men and women in the 25-55 age group.

Grafik Design: Develop a visually striking design that grabs attention in online retail environments like Kestrio.

Visuals: glass of water (or symbolic) and sticks (powder) just like benchmark brand aquelle.

Design Elements
Use colours that are inside the Vito-Prime Logo, attached.
Product will be available in 3 flavours. Lemon=yellow, Orange=orange, Black Currant=purple

Typography: Utilize strong, clean, and modern fonts. Ensure readability and create a sense of strength, endurance and reliability.

The product will be available in 3 flavours: Lemon, Orange and Johannisbeere

We look forward to seeing your creative ideas and innovative designs for our Vito Prime brand packaging.

```html
<!DOCTYPE html>
<html lang="en">
<head>
<meta charset="utf-8">
<title>Vito Prime Hydration Booster Packaging</title>
<link href="https://fonts.googleapis.com/css2?family=Montserrat:wght@400;500;600;800&display=swap" rel="stylesheet">
<style>
  :root {
    --bg: #c9c9c9;
    --blue: #2233a6;
    --blue-dark: #1a2790;
    --orange: #f26a1b;
    --orange-light: #f7892a;
    --white: #f7f7f5;
    --grey-text: #555c63;
    --yellow: #f1e51c;
    --line: #8d9196;
  }
  * { box-sizing: border-box; margin: 0; padding: 0; }
  html, body { width: 1200px; height: 800px; overflow: hidden; }
  body { background: var(--bg); font-family: "Montserrat", sans-serif; position: relative; }

  /* Pouch */
  .pouch { position: absolute; left: 210px; top: 128px; width: 490px; height: 560px; }
  .pouch-shape { position: absolute; inset: 0; }
  .count-badge {
    position: absolute; left: 45px; top: 92px; display: flex; align-items: center;
    border: 1.5px solid var(--white); border-radius: 2px; padding: 1px 4px; color: var(--white); gap: 3px;
  }
  .count-badge .count-number { font-weight: 800; font-size: 20px; color: var(--blue); line-height: 1; }
  .count-badge .count-label { font-size: 8.5px; font-weight: 500; line-height: 1.05; }
  .count-detail { position: absolute; left: 46px; top: 120px; font-size: 7.5px; font-weight: 500; color: var(--white); }

  .brand { position: absolute; left: 150px; top: 118px; width: 190px; text-align: center; z-index: 2; }
  .brand-name { font-weight: 800; font-size: 38px; color: var(--yellow); line-height: 1; letter-spacing: -0.5px; }
  .brand-since { font-size: 10px; font-weight: 500; color: var(--yellow); margin-top: 8px; }

  .title { position: absolute; left: 45px; top: 272px; color: var(--grey-text); }
  .title-main { font-weight: 800; font-size: 33px; line-height: 1; letter-spacing: -0.3px; }
  .title-sub { font-weight: 400; font-size: 36px; line-height: 1.02; }
  .tagline { font-size: 10px; font-weight: 500; color: var(--orange); margin-top: 6px; }

  .benefits { position: absolute; left: 52px; top: 376px; width: 102px; list-style: none; }
  .benefits li {
    display: flex; align-items: center; gap: 8px; height: 29px;
    border-top: 1px solid var(--line); color: var(--grey-text); font-size: 14px; font-weight: 500;
  }
  .benefits li:last-child { border-bottom: 1px solid var(--line); }
  .benefits svg { width: 14px; height: 14px; flex: none; }

  .pour-art {
    position: absolute; left: 345px; top: 62px; width: 135px; height: 215px;
    background: linear-gradient(200deg, rgba(34,51,166,0.55) 0%, rgba(240,240,240,0.6) 45%, rgba(242,106,27,0.55) 100%);
    border-radius: 6px;
  }
  .hero-art {
    position: absolute; left: 288px; top: 284px; width: 118px; height: 258px;
    background: linear-gradient(180deg, rgba(225,225,228,0.9) 0%, rgba(242,106,27,0.7) 60%, rgba(245,160,40,0.95) 100%);
    border-radius: 6px;
  }
  .flavour-tag {
    position: absolute; left: 408px; top: 452px; transform-origin: left top; transform: rotate(-90deg);
    font-weight: 800; font-size: 19px; color: var(--orange); letter-spacing: 0.5px; z-index: 2;
  }
  .pouch-footer {
    position: absolute; left: 60px; top: 508px; width: 180px; text-align: center;
    color: var(--white); font-size: 8.5px; font-weight: 500; line-height: 1.35;
  }

  /* Stick pack */
  .stick {
    position: absolute; left: 600px; top: 410px; width: 480px; height: 82px;
    transform: rotate(-90deg); overflow: hidden; border-radius: 2px;
    display: flex;
  }
  .stick-end { width: 48px; background: linear-gradient(90deg, var(--orange) 0%, var(--orange-light) 100%); display: flex; align-items: center; justify-content: center; color: var(--white); font-weight: 500; font-size: 12px; }
  .stick-body { width: 292px; background: var(--white); position: relative; }
  .stick-head { flex: 1; background: var(--blue); display: flex; align-items: center; justify-content: center; }
  .stick-head .brand-name { font-size: 24px; white-space: nowrap; }
  .stick-title { position: absolute; right: 10px; top: 4px; color: var(--grey-text); line-height: 1; }
  .stick-title .title-main { font-size: 21px; }
  .stick-title .title-sub { font-size: 22px; font-weight: 400; }
  .stick-title .tagline { font-size: 6px; color: var(--grey-text); margin-top: 2px; }
  .stick-flavour {
    position: absolute; left: 128px; top: 61px; background: var(--orange); color: var(--white);
    font-weight: 800; font-size: 9px; padding: 1px 6px; border-radius: 8px;
  }
  .stick-benefits { position: absolute; left: 66px; top: 8px; list-style: none; width: 58px; }
  .stick-benefits li { font-size: 7.5px; color: var(--grey-text); border-bottom: 0.5px solid var(--line); padding: 3px 0; }
  .stick-footer { position: absolute; left: 4px; top: 22px; width: 60px; font-size: 5.5px; color: var(--grey-text); line-height: 1.3; text-align: center; }
</style>
</head>
<body>

<section class="pouch" aria-label="Vito Prime Hydration Booster pouch, front">
  <svg class="pouch-shape" viewBox="0 0 490 560" preserveAspectRatio="none" aria-hidden="true">
    <defs>
      <linearGradient id="pouchBlue" x1="0" y1="0" x2="1" y2="1">
        <stop offset="0" stop-color="#2a3db5"/>
        <stop offset="1" stop-color="#1a2790"/>
      </linearGradient>
      <linearGradient id="pouchOrange" x1="0" y1="0" x2="1" y2="0">
        <stop offset="0" stop-color="#f7892a"/>
        <stop offset="1" stop-color="#e8531a"/>
      </linearGradient>
    </defs>
    <rect x="0" y="0" width="490" height="560" rx="4" fill="url(#pouchBlue)"/>
    <path d="M0,232 L40,222 L70,230 L120,226 L150,240 L190,224 L240,218 L262,236 L300,226 L350,238 L400,224 L450,232 L490,226 L490,560 L0,560Z" fill="#f7f7f5"/>
    <path d="M0,494 L60,486 L110,496 L170,486 L220,492 L260,482 L300,490 L350,478 L410,488 L490,476 L490,560 L0,560Z" fill="url(#pouchOrange)"/>
    <polygon points="38,0 108,0 108,155 73,140 38,155" fill="url(#pouchOrange)"/>
  </svg>

  <div class="count-badge"><span class="count-number">20</span><span class="count-label">Stick<br>Packs</span></div>
  <div class="count-detail">20 Sticks 12.9g</div>

  <div class="brand">
    <div class="brand-name">Vito<br>Prime</div>
    <div class="brand-since">since 1992</div>
  </div>

  <div class="title">
    <div class="title-main">HYDRATION</div>
    <div class="title-sub">BOOSTER</div>
    <div class="tagline">Premium Isotonic Electrolyte Drink</div>
  </div>

  <ul class="benefits">
    <li><svg viewBox="0 0 14 14" aria-hidden="true"><circle cx="7" cy="7" r="6" fill="none" stroke="#8d9196"/><path d="M7 4v6M4 7h6" stroke="#8d9196"/></svg>Refresh</li>
    <li><svg viewBox="0 0 14 14" aria-hidden="true"><path d="M2 9q2.5-2 5 0t5 0M2 12q2.5-2 5 0t5 0M4 2l-1 3h2zM7 2l-1 3h2zM10 2l-1 3h2z" fill="none" stroke="#8d9196"/></svg>Replenish</li>
    <li><svg viewBox="0 0 14 14" aria-hidden="true"><rect x="4" y="2" width="6" height="11" rx="1" fill="none" stroke="#8d9196"/><path d="M8 5l-2 3h2l-2 3" fill="none" stroke="#8d9196"/></svg>Recharge</li>
  </ul>

  <div class="pour-art" role="img" aria-label="Tilted stick pack pouring a stream of orange powder downward"></div>
  <div class="hero-art" role="img" aria-label="Glass of water with orange powder swirling in it and an orange slice, with orange halftone dots around"></div>
  <div class="flavour-tag">ORANGE</div>

  <div class="pouch-footer">Nutritional Expertise Since 1992.<br>DIETARY SUPLEMENT</div>
</section>

<section class="stick" aria-label="Vito Prime Hydration Booster stick pack">
  <div class="stick-end">12.9g</div>
  <div class="stick-body">
    <div class="stick-footer">Nutritional Expertise Since 1992.<br>DIETARY SUPLEMENT</div>
    <ul class="stick-benefits">
      <li>Refresh</li>
      <li>Replenish</li>
      <li>Recharge</li>
    </ul>
    <div class="stick-flavour">ORANGE</div>
    <div class="stick-title">
      <div class="title-main">HYDRATION</div>
      <div class="title-sub">BOOSTER</div>
      <div class="tagline">Premium Isotonic Electrolyte Drink</div>
    </div>
  </div>
  <div class="stick-head"><div class="brand-name">Vito Prime</div></div>
</section>

</body>
</html>
```